Modern business card for triathlon training business in Australia

We need a business card design for our triathlon training company.

Pace with Us Fitness is an Australian business, owned by women, run for women. Pace with Us Fitness helps women prepare or improve triathlon skills and confidence through triathlon camps completely designed for women.

Our camps focus on preparing women both physically and mentally for their next (or first!) triathlon.

You can see our website www.pacewithusfitness.com.au for more info about our business and our style.

We've attached two of our logos and are happy to consider a design that utilised either colour scheme with the teal colour being our 'feature' colour. We don't want overly feminine cards but rather cards that are professional and neat. If the inclusion of any pictures/art is warranted, this should be focused on our swim/ride/run theme and in that specific order (swim/ride/run).

The business card needs to be a printable design and the contact details will need to change for our two employees.

Target Market(s)

Female clients and partners/vendors/sponsors that we work with in the triathlon industry

Industry/Entity Type

Fitness

Contact Information for Business Card

Pace with Us Fitness (business name)
Nina Carver
Business Director
Mobile: 0438 916 207
Email: nina@pacewithusfitness.com.au
www.pacewithusfitness.com.au

Second business card:
Pace with Us Fitness
Bel Stray
Coaching Director
Mobile: 0459 260 718
Email: bel@pacewithusfitness.com.au

Font styles to use
Serif
Sans Serif

Requirements
Must have
• Core contact details above, our logo and be a printable design
Should not have
• Pink
• Cursive/script fonts

```html
<!DOCTYPE html>
<html lang="en">
<head>
<meta charset="utf-8">
<title>Pace with Us Fitness – Business Cards</title>
<link rel="stylesheet" href="https://fonts.googleapis.com/css2?family=Montserrat:wght@300;400;500&display=swap">
<style>
  :root {
    --backdrop: #5fa7bb;
    --teal: #5cb9cd;
    --teal-deep: #4aa6bb;
    --card-dark: #1f1f20;
    --white: #ffffff;
    --text-soft: #e8eef0;
  }
  * { box-sizing: border-box; margin: 0; padding: 0; }
  html, body {
    width: 1200px;
    height: 814px;
    overflow: hidden;
  }
  body {
    background: var(--backdrop);
    font-family: "Montserrat", Arial, sans-serif;
    display: flex;
    align-items: center;
    justify-content: center;
    gap: 40px;
  }
  .business-card {
    width: 540px;
    height: 330px;
    display: flex;
    border-radius: 4px;
    overflow: hidden;
    box-shadow: 0 14px 30px rgba(0, 0, 0, 0.22);
  }
  .brand-panel {
    width: 40%;
    background: var(--teal);
    padding: 34px 22px;
    border-right: 3px solid var(--white);
  }
  .brand-name {
    display: flex;
    align-items: center;
    gap: 10px;
    color: var(--white);
    font-weight: 500;
    font-size: 19px;
    line-height: 1.15;
    letter-spacing: 0.02em;
  }
  .brand-square {
    flex: none;
    width: 16px;
    height: 16px;
    background: var(--white);
  }
  .details-panel {
    flex: 1;
    background: var(--card-dark);
    padding: 34px 28px 30px;
    display: flex;
    flex-direction: column;
    justify-content: space-between;
  }
  .discipline-icons {
    display: flex;
    gap: 12px;
    justify-content: flex-end;
  }
  .discipline-icon {
    width: 36px;
    height: 36px;
    border-radius: 7px;
    background: linear-gradient(135deg, var(--teal), var(--teal-deep));
  }
  .contact-name {
    font-size: 15px;
    font-weight: 400;
    color: var(--teal);
    margin-bottom: 8px;
  }
  .contact-role { color: var(--white); }
  .contact-list {
    list-style: none;
    font-size: 12px;
    font-weight: 300;
    line-height: 1.7;
    color: var(--text-soft);
  }
  .contact-label {
    display: inline-block;
    width: 16px;
    color: var(--teal);
    font-weight: 400;
  }
</style>
</head>
<body>

  <article class="business-card">
    <div class="brand-panel">
      <div class="brand-name"><span class="brand-square"></span>Pace with Us Fitness</div>
    </div>
    <div class="details-panel">
      <div class="discipline-icons">
        <div class="discipline-icon" role="img" aria-label="Swim icon"></div>
        <div class="discipline-icon" role="img" aria-label="Ride icon"></div>
        <div class="discipline-icon" role="img" aria-label="Run icon"></div>
      </div>
      <div class="contact-block">
        <p class="contact-name">Nina Carver <span class="contact-role">Business Director</span></p>
        <ul class="contact-list">
          <li><span class="contact-label">M</span>0438 916 207</li>
          <li><span class="contact-label">E</span>nina@pacewithusfitness.com.au</li>
          <li><span class="contact-label">W</span>pacewithusfitness.com.au</li>
        </ul>
      </div>
    </div>
  </article>

  <article class="business-card">
    <div class="brand-panel">
      <div class="brand-name"><span class="brand-square"></span>Pace with Us Fitness</div>
    </div>
    <div class="details-panel">
      <div class="discipline-icons">
        <div class="discipline-icon" role="img" aria-label="Swim icon"></div>
        <div class="discipline-icon" role="img" aria-label="Ride icon"></div>
        <div class="discipline-icon" role="img" aria-label="Run icon"></div>
      </div>
      <div class="contact-block">
        <p class="contact-name">Bel Stray <span class="contact-role">Coaching Director</span></p>
        <ul class="contact-list">
          <li><span class="contact-label">M</span>0459 260 718</li>
          <li><span class="contact-label">E</span>bel@pacewithusfitness.com.au</li>
          <li><span class="contact-label">W</span>pacewithusfitness.com.au</li>
        </ul>
      </div>
    </div>
  </article>

</body>
</html>
```